Dean harlowe realestate

We want something complete different to our website now and something that will stand out this is our website http://deanharlowerealestate-demo.com/

our company website for my boss is www.stevenorrick-demo.com

please note this website is being made for dean harlowe not steven orrick

something similar to our company website but has to be in the branding of dean harlowe realestate

```html
<!DOCTYPE html>
<html lang="en">
<head>
<meta charset="utf-8">
<title>Dean Harlowe Property</title>
<link href="https://fonts.googleapis.com/css2?family=Roboto:wght@300;400;500;700&family=Open+Sans:ital,wght@0,400;0,600;1,400&display=swap" rel="stylesheet">
<style>
:root{
  --orange:#ff6a0f;
  --ink:#1f1f1f;
  --text:#333333;
  --muted:#8a8a8a;
  --white:#ffffff;
  --light:#e9e9e9;
  --dark:#555555;
  --footer-bar:#e4e4e4;
}
*{margin:0;padding:0;box-sizing:border-box}
html,body{width:1200px;height:3435px;overflow:hidden;background:var(--white)}
body{font-family:'Roboto',sans-serif;color:var(--text)}
.page{position:relative;width:1200px;height:3435px;overflow:hidden}
.abs{position:absolute}

/* header */
.site-header{position:absolute;left:0;top:0;width:1200px;height:88px;background:var(--white);z-index:3}
.brand{position:absolute;left:121px;top:22px;height:46px;padding:0 10px;display:flex;align-items:center;font-size:30px;font-weight:400;color:var(--ink)}
.main-nav{position:absolute;left:496px;top:34px;display:flex;gap:26px;font-size:16px;color:var(--text)}
.main-nav a{color:inherit;text-decoration:none}
.main-nav .active{color:var(--ink);font-weight:500}
.social{position:absolute;left:1016px;top:34px;display:flex;gap:18px}
.social span{width:18px;height:18px;border-radius:50%;background:#555}

/* hero */
.hero-photo{position:absolute;left:0;top:88px;width:1200px;height:600px;
  background:linear-gradient(180deg,#3d4a35 0%,#4e5c3a 40%,#6c7a44 70%,#5d6a3a 100%)}
.hero-shape{position:absolute;left:0;top:580px;width:1200px;height:110px}
.play{position:absolute;left:552px;top:240px;width:80px;height:80px}
.hero-title{position:absolute;left:0;top:340px;width:1200px;text-align:center;color:var(--white);font-weight:400;line-height:1.2}
.hero-title .small{display:block;font-size:34px}
.hero-title .big{display:block;font-size:40px;font-weight:500}

/* properties */
.section-title{position:absolute;left:0;width:1200px;text-align:center;font-size:28px;font-weight:500;color:var(--ink);text-transform:uppercase}
.property{position:absolute;overflow:hidden}
.property .photo{position:absolute;inset:0}
.property .label{position:absolute;left:36px;bottom:22px;color:var(--white);font-size:18px;line-height:1.45;letter-spacing:.3px;text-transform:uppercase}

/* appraisal */
.appraisal-band{position:absolute;left:0;top:1545px;width:1200px;height:490px}
.appraisal-intro{position:absolute;left:117px;top:1642px;width:284px;height:206px;border-top:2px solid var(--white);border-bottom:2px solid var(--white);color:var(--white);padding:24px 10px 0 10px}
.appraisal-intro h2{font-size:34px;font-weight:400;line-height:1.1;text-transform:uppercase}
.appraisal-intro p{margin-top:14px;font-size:14px;line-height:1.7}
.field-label{position:absolute;color:var(--white);font-size:14px;font-weight:500;text-transform:uppercase}
.field{position:absolute;background:var(--white)}
.send{position:absolute;left:456px;top:1901px;width:128px;height:41px;background:#111;color:var(--white);font-size:16px;font-weight:500;display:flex;align-items:center;justify-content:center}

/* testimonials */
.testimonial-bg{position:absolute;left:0;top:1960px;width:1200px;height:560px;background:var(--light)}
.quote-card{position:absolute;top:2148px;width:465px;height:236px;background:var(--white);box-shadow:0 1px 4px rgba(0,0,0,.12)}
.quote-card .mark{position:absolute;font-family:Georgia,serif;font-size:60px;color:#777;line-height:1}
.quote-card p{position:absolute;left:74px;top:28px;width:350px;font-family:'Open Sans',sans-serif;font-style:italic;font-size:13px;line-height:1.85;color:#666}
.reviewer{position:absolute;left:52px;display:flex;align-items:center;gap:14px}
.reviewer .avatar{width:46px;height:46px;border-radius:50%}
.reviewer b{display:block;font-family:'Open Sans',sans-serif;font-size:15px;font-weight:600;color:#333}
.reviewer small{font-family:'Open Sans',sans-serif;font-size:13px;color:#999}
.slider-dots{position:absolute;left:528px;top:2424px;display:flex;gap:6px;align-items:center}
.slider-dots .arrow{width:20px;height:20px;border-radius:50%;background:#111}
.slider-dots .dot{width:10px;height:10px;border-radius:50%;background:#888}
.slider-dots .dot.on{background:#111}

/* contact */
.contact-band{position:absolute;left:0;top:2440px;width:1200px;height:520px}
.map{position:absolute;left:188px;top:2638px;width:453px;height:254px;background:linear-gradient(135deg,#ececec,#d6d6d6)}
.contact-info{position:absolute;left:698px;color:var(--white);display:flex;gap:20px}
.contact-info svg{flex:none;margin-top:2px}
.contact-info .key{display:block;font-size:15px;color:#cfcfcf;text-transform:uppercase}
.contact-info .val{display:block;font-size:19px;line-height:1.5}

/* footer */
.footer-heading{position:absolute;top:3060px;font-size:21px;font-weight:500;color:var(--ink);text-transform:uppercase}
.footer-links{position:absolute;left:128px;top:3106px;list-style:none;font-size:15px;line-height:34.5px;color:var(--text)}
.recent-posts{position:absolute;left:348px;top:3110px;width:330px;font-size:15px;line-height:1.55;color:var(--text)}
.recent-posts p{margin-bottom:17px}
.footer-form{position:absolute;left:747px;top:3034px;width:309px;height:280px;background:var(--orange);border-radius:10px;color:var(--white);padding:24px 40px}
.footer-form h3{font-size:21px;font-weight:500;text-transform:uppercase}
.footer-form .line{font-size:14px;padding:12px 0 8px;border-bottom:1px solid rgba(255,255,255,.8);margin-top:6px}
.footer-form .pill{width:110px;height:40px;border-radius:20px;background:#444;color:var(--white);display:flex;align-items:center;justify-content:center;font-size:16px;margin-top:22px}
.bottom-bar{position:absolute;left:0;top:3378px;width:1200px;height:57px;background:var(--footer-bar);color:#888;font-size:13px;text-align:center;line-height:57px}
</style>
</head>
<body>
<div class="page">

  <header class="site-header">
    <div class="brand">Dean Harlowe Property</div>
    <nav class="main-nav">
      <a class="active">HOME</a><a>FOR SALE</a><a>AGENTS</a><a>BOOK APPRAISAL</a><a>CONTACT</a>
    </nav>
    <div class="social" aria-label="Social links"><span></span><span></span></div>
  </header>

  <section class="hero">
    <div class="hero-photo" role="img" aria-label="Video still of the agent standing on a park lawn between carved timber posts"></div>
    <svg class="hero-shape" viewBox="0 0 1200 110" width="1200" height="110" aria-hidden="true">
      <polygon points="0,16 600,102 1200,20 1200,110 0,110" fill="#ffffff"/>
      <polygon points="0,16 600,102 600,96 0,0" fill="#ff6a0f"/>
      <polygon points="600,102 1200,20 1200,14 600,96" fill="#ff6a0f" opacity="0"/>
    </svg>
    <svg class="play" viewBox="0 0 80 80" aria-hidden="true">
      <circle cx="40" cy="40" r="37" fill="#ffffff"/>
      <circle cx="40" cy="40" r="31" fill="none" stroke="#222" stroke-width="2"/>
      <polygon points="32,26 32,54 55,40" fill="#111"/>
    </svg>
    <h1 class="hero-title"><span class="small">WELCOME TO</span><span class="big">DEAN HARLOWE PROPERTY</span></h1>
  </section>

  <section class="sold">
    <h2 class="section-title" style="top:745px">Latest Properties Sold</h2>
    <div class="property" style="left:117px;top:808px;width:643px;height:325px">
      <div class="photo" role="img" aria-label="Brick home with red tiled roof at dusk" style="background:linear-gradient(180deg,#8a8fb8 0%,#c7a6a8 35%,#8f5a4a 65%,#3a3330 100%)"></div>
      <div class="label">44 Fernley Street<br>Eastbrook, 6199</div>
    </div>
    <div class="property" style="left:774px;top:808px;width:307px;height:325px">
      <div class="photo" role="img" aria-label="Two-storey white home lit at dusk" style="background:linear-gradient(180deg,#5d7aa8 0%,#b9c2cf 40%,#8a6a4a 75%,#2c2a28 100%)"></div>
      <div class="label">19 Arden Street<br>Westmoor, 6198</div>
    </div>
    <div class="property" style="left:117px;top:1152px;width:307px;height:295px">
      <div class="photo" role="img" aria-label="Cream rendered townhouse with balcony" style="background:linear-gradient(180deg,#6f9fd8 0%,#d8c7aa 45%,#a77a5a 75%,#5a3a30 100%)"></div>
      <div class="label">4/25 Coral Road<br>Greenvale, 6197</div>
    </div>
    <div class="property" style="left:447px;top:1152px;width:306px;height:295px">
      <div class="photo" role="img" aria-label="Brick home with red roof under evening sky" style="background:linear-gradient(180deg,#23407a 0%,#5a6f9a 35%,#8a5a4a 70%,#2a2623 100%)"></div>
      <div class="label">65 Barley Street<br>Eastbrook, 6199</div>
    </div>
    <div class="property" style="left:774px;top:1152px;width:307px;height:295px">
      <div class="photo" role="img" aria-label="Modern grey and white single-storey home" style="background:linear-gradient(180deg,#6d9bd2 0%,#c9d3dd 40%,#9a9a98 72%,#4a4a48 100%)"></div>
      <div class="label">21 Calloway Street<br>Eastbrook, 6199</div>
    </div>
  </section>

  <div class="testimonial-bg" role="img" aria-label="Light grey geometric line pattern background"></div>

  <section class="appraisal">
    <svg class="appraisal-band" viewBox="0 0 1200 490" aria-hidden="true">
      <polygon points="0,0 1200,0 1200,425 600,488 0,425" fill="#ff6a0f"/>
    </svg>
    <div class="appraisal-intro">
      <h2>Book an<br>Appraisal</h2>
      <p>Class aptent taciti sociosqu ad litora torquent per conubia nostra per inceptos hymenaeos Proin</p>
    </div>
    <span class="field-label" style="left:456px;top:1627px">Name</span>
    <div class="field" style="left:456px;top:1649px;width:286px;height:37px"></div>
    <span class="field-label" style="left:760px;top:1627px">Email</span>
    <div class="field" style="left:760px;top:1649px;width:285px;height:37px"></div>
    <span class="field-label" style="left:456px;top:1702px">Phone</span>
    <div class="field" style="left:456px;top:1724px;width:286px;height:37px"></div>
    <span class="field-label" style="left:760px;top:1702px">Address</span>
    <div class="field" style="left:760px;top:1724px;width:285px;height:37px"></div>
    <span class="field-label" style="left:456px;top:1778px">Message</span>
    <div class="field" style="left:456px;top:1802px;width:589px;height:83px"></div>
    <div class="send">SEND</div>
  </section>

  <section class="testimonials">
    <h2 class="section-title" style="top:2084px;font-size:26px">What Our Client Say</h2>
    <article class="quote-card" style="left:98px">
      <span class="mark" style="left:30px;top:26px">&ldquo;</span>
      <p>I found Dean to be different from most agents, in that he listened, and set a marketing program to suit the special features of our property. Eager to do anything to assist with a positive outcome, I'd recommend Dean for properties in the local area. <span style="font-family:Georgia,serif;font-size:34px;font-style:normal;color:#777;line-height:0">&rdquo;</span></p>
      <div class="reviewer" style="top:165px">
        <div class="avatar" role="img" aria-label="Client portrait" style="background:#b8a48c"></div>
        <div><b>Owen</b><small>Westmoor, 6198</small></div>
      </div>
    </article>
    <article class="quote-card" style="left:595px">
      <span class="mark" style="left:30px;top:26px">&ldquo;</span>
      <p>Dean is very talented and highly ethical person who provides a high standard of customer service both during the transaction and after. <span style="font-family:Georgia,serif;font-size:34px;font-style:normal;color:#777;line-height:0">&rdquo;</span></p>
      <div class="reviewer" style="top:160px">
        <div class="avatar" role="img" aria-label="Client portrait" style="background:#a9a9a9"></div>
        <div><b>Miles</b><small>Eastbrook, 6199</small></div>
      </div>
    </article>
    <div class="slider-dots">
      <span class="arrow"></span><span class="dot on"></span><span class="dot"></span><span class="dot"></span><span class="dot"></span><span class="arrow"></span>
    </div>
  </section>

  <section class="contact">
    <svg class="contact-band" viewBox="0 0 1200 520" role="img" aria-label="Greyscale photo of a large two-storey home">
      <defs>
        <linearGradient id="contactTone" x1="0" y1="0" x2="1" y2="1">
          <stop offset="0" stop-color="#6a6a6a"/>
          <stop offset=".5" stop-color="#4e4e4e"/>
          <stop offset="1" stop-color="#3c3c3c"/>
        </linearGradient>
      </defs>
      <polygon points="0,20 600,60 1200,20 1200,470 600,518 0,455" fill="url(#contactTone)"/>
    </svg>
    <h2 class="section-title" style="top:2572px;color:#fff;font-size:27px">Contact Us</h2>
    <div class="map" role="img" aria-label="Street map showing the office location"></div>

    <div class="contact-info" style="top:2638px">
      <svg width="20" height="26" viewBox="0 0 20 26" aria-hidden="true"><path d="M10 1a8 8 0 0 0-8 8c0 6 8 16 8 16s8-10 8-16a8 8 0 0 0-8-8z" fill="none" stroke="#fff" stroke-width="2"/><circle cx="10" cy="9" r="3" fill="#fff"/></svg>
      <div><span class="key">Address</span><span class="val">Suite 12, 48 Marlowe Parade,<br>Eastbrook, WA 6199 Australia</span></div>
    </div>
    <div class="contact-info" style="top:2745px">
      <svg width="22" height="18" viewBox="0 0 22 18" aria-hidden="true"><rect x="1" y="1" width="20" height="16" fill="none" stroke="#fff" stroke-width="2"/><path d="M1 2l10 8 10-8" fill="none" stroke="#fff" stroke-width="2"/></svg>
      <div><span class="key">Email</span><span class="val">dean@stevenorrick-demo.com</span></div>
    </div>
    <div class="contact-info" style="top:2815px">
      <svg width="22" height="22" viewBox="0 0 22 22" aria-hidden="true"><path d="M5 1l4 5-2 3c1 3 3 5 6 6l3-2 5 4-3 4C9 21 1 13 1 4z" fill="none" stroke="#fff" stroke-width="2" stroke-linejoin="round"/></svg>
      <div><span class="key">Phone</span><span class="val">0400 555 019</span></div>
    </div>
  </section>

  <footer>
    <h3 class="footer-heading" style="left:121px">Company</h3>
    <ul class="footer-links">
      <li>About Us</li><li>For Sale</li><li>Agents</li><li>Book Appraisal</li><li>Contact Us</li>
    </ul>
    <h3 class="footer-heading" style="left:346px">Recent Posts</h3>
    <div class="recent-posts">
      <p>Class aptent taciti sociosqu ad litora torquent per conubia nostra per inceptos</p>
      <p>Praesent elementum elit at tellus nec ultricies sit amet porttito</p>
      <p>Duis quam Nam eget lacus Aliquam erat volutpat Quisque dignissim congue</p>
    </div>
    <div class="footer-form">
      <h3>Contact Form</h3>
      <div class="line">Full Name</div>
      <div class="line">Email address</div>
      <div class="line">Phone</div>
      <div class="pill">Send</div>
    </div>
    <div class="bottom-bar">&copy; 2018 Company Name &nbsp;All right reserved</div>
  </footer>

</div>
</body>
</html>
```